Torvenu Business Card Design Project

We need a business card design for torvenu.com a company based in Berlin, Germany.

?Torvenu is marketplace that enables people all over the world to monetize and exchange their individual knowledge and language skills through interactive video sessions. User are matched by their interests.

On Torvenu everybody can be student or teacher (seller or buyer).

We would love to see designs that use or main color blue and green. The design should communicate what Torvenu enables - see my notice above.

Looking so forward to your designs
Cheers from Berlin,
Konrad

Target Market(s)

globally

Industry/Entity Type

Teacher

Requirements
Must have
• Konrad Wielert
CEO
Torvenu.com

Torvenu e-Services GmbH
Lindgrubweg 27
10117 Berlin

Fon: +49 30 481 906 27 14
Mobile: 49 171 57 04 91 3
E-Mail: k.wielert@torvenu.com
Web: www.torvenu.com

```html
<!DOCTYPE html>
<html lang="en">
<head>
<meta charset="utf-8">
<title>Torvenu Business Card</title>
<link rel="stylesheet" href="https://fonts.googleapis.com/css2?family=Michroma&display=swap">
<style>
  :root {
    --backdrop: #040404;
    --card: #111718;
    --card-light: #6f7778;
    --green: #99ee11;
    --blue: #44c8f5;
    --grey: #6a7274;
  }
  html, body {
    margin: 0;
    padding: 0;
    overflow: hidden;
    background: var(--backdrop);
  }
  .canvas {
    position: relative;
    width: 1200px;
    height: 1000px;
    background: var(--backdrop);
    overflow: hidden;
    font-family: "Michroma", sans-serif;
  }
  .card {
    position: absolute;
    top: 178px;
    width: 449px;
    height: 747px;
    overflow: hidden;
  }
  .card-front {
    left: 111px;
    border-top-right-radius: 110px 110px;
    background: linear-gradient(90deg, var(--card-light) 0%, #3e4748 18%, #1d2526 40%, var(--card) 62%, var(--card) 100%);
  }
  .accent-stripe {
    position: absolute;
    left: 0;
    top: 0;
    width: 61px;
    height: 100%;
    background: var(--green);
  }
  .card-back {
    left: 643px;
    top: 175px;
    height: 750px;
    border-top-left-radius: 110px 110px;
    background: linear-gradient(90deg, var(--card) 0%, var(--card) 38%, #1d2829 56%, #3e4a4b 74%, var(--card-light) 100%);
  }
  .holder {
    position: absolute;
    right: 24px;
    text-align: right;
    white-space: nowrap;
  }
  .holder-name {
    top: 112px;
    margin: 0;
    font-size: 31px;
    font-weight: 400;
    color: var(--green);
    letter-spacing: 0.5px;
  }
  .holder-name .initial { color: var(--blue); font-size: 38px; }
  .holder-role {
    top: 166px;
    font-size: 26px;
    color: var(--grey);
  }
  .holder-site {
    top: 207px;
    font-size: 26px;
    color: var(--grey);
  }
  .company-address {
    position: absolute;
    left: 71px;
    top: 518px;
    margin: 0;
    font-style: normal;
    font-size: 18px;
    line-height: 25px;
    color: var(--grey);
    white-space: nowrap;
  }
  .brand-mark {
    position: absolute;
    left: 24px;
    top: 640px;
    display: flex;
    align-items: center;
    gap: 14px;
  }
  .brand-mark .square {
    width: 34px;
    height: 34px;
    background: var(--blue);
  }
  .brand-mark .word {
    font-size: 46px;
    color: var(--grey);
    line-height: 1;
  }
  .brand-center {
    position: absolute;
    left: 0;
    right: 0;
    top: 350px;
    text-align: center;
    font-size: 40px;
    color: var(--blue);
  }
  .contact-list {
    position: absolute;
    left: 67px;
    top: 584px;
    margin: 0;
    padding: 0;
    list-style: none;
    font-size: 16px;
    white-space: nowrap;
  }
  .contact-list li { height: 37.5px; }
  .contact-list .label { color: var(--green); }
  .contact-list .value { color: var(--blue); }
</style>
</head>
<body>
<main class="canvas">
  <section class="card card-front">
    <div class="accent-stripe"></div>
    <h1 class="holder holder-name"><span class="initial">K</span>onrad Wielert</h1>
    <div class="holder holder-role">CEO</div>
    <div class="holder holder-site">Torvenu.com</div>
    <address class="company-address">
      Torvenu e-Services GmbH<br>
      Lindgrubweg 27<br>
      10117 Berlin
    </address>
    <div class="brand-mark">
      <span class="square"></span>
      <span class="word">torvenu</span>
    </div>
  </section>

  <section class="card card-back">
    <div class="brand-center">Torvenu</div>
    <ul class="contact-list">
      <li><span class="label">Fon:</span> <span class="value">+49 30 481 906 27 14</span></li>
      <li><span class="label">Mobile:</span> <span class="value">49 171 57 04 91 3</span></li>
      <li><span class="label">E-Mail:</span> <span class="value">k.wielert@torvenu.com</span></li>
      <li><span class="label">Web:</span> <span class="value">www.torvenu.com</span></li>
    </ul>
  </section>
</main>
</body>
</html>
```